A5 Patient Information Booklet (Chiropractic Clinic) 4-8 pages

Here’s a polished, professional rewrite of your full brief and content, with clearer structure, corrected language, and a premium tone:

---

**Project Title:** Premium Patient Information Brochure (Chiropractic & Wellness Clinic)

---

### **Overview**

We are a health and wellness clinic seeking a premium, high-end patient information brochure to provide following a patient’s initial consultation and first treatment.

The purpose of this booklet is to:

* Reinforce trust and professionalism
* Help patients understand what to expect next
* Encourage adherence to care recommendations
* Position the clinic as calm, expert-led, and results-driven

---

### **Format**

* 4–8 page booklet (A5 or similar size)
* Print-ready and digital versions required

---

### **Target Audience**

Patients who have just completed their initial consultation and may have begun treatment. They may already be experiencing physical or mental changes, so the brochure should guide, reassure, and educate them on what comes next.

---

### **Tone & Style**

* Premium, calm, and reassuring
* Modern wellness aesthetic (not overly clinical)
* Clean layout with minimal clutter
* Soft, neutral colour palette (whites, creams, muted greens, soft blues)
* Elegant typography (e.g. Montserrat / Lato)
* High-end, trustworthy, and professional feel

---

### **Key Messages**

#### 1. Listen to Your Body

Patients may feel different after treatment. Reassure them that this is normal and part of the healing process.

#### 2. Post-Treatment Advice

* Stay well hydrated
* Rest if needed
* Avoid overexertion if the body requires recovery

#### 3. Healing is a Journey (Core Concept)

A strong visual metaphor of a **“road to recovery”** or **journey** should be central to the design.

This journey should clearly illustrate three phases:

* **Phase 1: Initial Care (Weeks 1–6)**
Focus: Reducing pain/discomfort, calming the body, and initiating response to treatment

* **Phase 2: Corrective Care (Weeks 6–12)**
Focus: Addressing underlying issues, improving function, and creating lasting change

* **Phase 3: Wellness / Maintenance (Ongoing)**
Focus: Maintaining progress, preventing relapse, and supporting long-term wellbeing

**Important:**

* Emphasise that this is not a quick fix
* Progress requires time and consistency
* Each patient follows an individualised care plan
* The journey should feel structured, positive, and achievable

#### 4. Personalised Care

Reinforce that every treatment plan is tailored specifically to the individual.

#### 5. Professional Reassurance

Patients should feel confident they are in expert hands and supported throughout their journey.

---

### **Design Direction**

* Use imagery that reflects calmness, progression, and wellness (e.g. pathways, nature, soft gradients)
* Avoid generic stock imagery
* **Only use original clinic images from website and social media**
* Prioritise white space and clarity
* Aim for a luxury spa/medical hybrid aesthetic

---

## **Content Structure (Page-by-Page)**

### **Front Cover**

* Clean, minimal, premium design
* Clinic branding

---

### **Page 1: Patient Case Summary**

**Title:** *Welcome to Fernwell Practice*

Thank you for choosing Fernwell Practice.

This booklet is designed to guide you through:

* What we found during your initial consultation
* Your personalised recommended treatment plan
* Your road to recovery
* Long-term wellness care
* Why we take the approach we do

---

### **Page 2: Your Care Journey**

**Stage 1: Your Initial Consultation**

Today we completed a comprehensive assessment of your health and function, including:

* Full case history and discussion of your symptoms and goals
* Orthopaedic and neurological testing
* Postural and movement assessment
* Initial treatment (where appropriate)

**What this tells us:**

* How your body is currently functioning
* Where areas of stress or dysfunction may be present
* The most appropriate and effective path forward for your care

---

### **Page 3: Your Suggested Treatment Plan**

Based on today’s findings, your recommended care plan is:

**______ treatments over ______ weeks**

This should be viewed alongside your *Road to Recovery* to help you understand what to expect.

We have also discussed:

* Expected timelines for improvement
* Available payment options

**After Treatment:**
It is common to feel different following treatment. This is a normal response as your body begins to adapt and respond.

We recommend:

* Staying well hydrated
* Allowing time for rest and recovery
* Avoiding overexertion if your body feels it needs it

---

### **Page 4: What to Expect Next**

Healing is not always linear—it is a process that occurs over time.

Your care will typically progress through the following stages:

* **Relief Care**
Focused on reducing discomfort and calming the body

* **Corrective Care**
Focused on addressing underlying issues and improving function
(This phase may include prescribed exercises)

* **Maintenance / Wellness Care**
Focused on sustaining progress, preventing recurrence, and supporting long-term health

---

### **Page 5: Understanding Chiropractic Care**

**What is Chiropractic?**
Chiropractic care focuses on the relationship between the spine, nervous system, and overall body function.

By improving spinal movement and alignment, chiropractic care helps support the nervous system, allowing the body to function and heal more effectively.

**About Fernwell Practice**
At Fernwell Practice, our approach is centred around personalised, patient-focused care. We aim to not only relieve symptoms but to address underlying causes and support long-term wellbeing.

---

### **Back Page**

* Clinic contact details
* Website
* Social media icons/handles

**Closing Message:**
“A healthier, stronger you—supported every step of the way.”

---

### **Deliverables**

* Print-ready PDF
* Editable source files

---

### **Additional Notes**

* The brochure should feel valuable and worth keeping
* Encourage long-term care in a subtle, non-pushy way
* Maintain clarity, readability, and strong visual hierarchy
* Balance professionalism with warmth and approachability

---

If you’d like, I can also turn this into **actual brochure copy (fully written, patient-facing text)** or help you refine it further for a designer.

Target Market(s)

Existing patients who want to feel better and look after themselves that is given after their initil consultation appointment

Industry/Entity Type

Chiropractic, wellness, health

Font styles to use
Other font styles liked:
• Montserrat or Lato

Colors
0094D4
00A9DD
6FCCEA
C7EBF8
E9F6FB
00AB8E
00BBA5
67D7C9
C6EFE9
E9F9F6
6B429C
8869AF
B7A5CE
E3DAEB
F3F0F8

Requirements
Must have
• my own photos, look premium wellness, be clear and simple to understand for patients journey or what to expect next and over time
Nice to have
• USe my social media/website for ideas
Should not have
• generic photos and images

```html
<!DOCTYPE html>
<html lang="en">
<head>
<meta charset="utf-8">
<title>Fernwell Practice – Patient Care Booklet</title>
<link href="https://fonts.googleapis.com/css2?family=Playfair+Display:wght@400;600;700&family=Lato:wght@400;700&family=Great+Vibes&display=swap" rel="stylesheet">
<style>
  :root{
    --backdrop:#5ec4b3;
    --teal:#3db5a5;
    --teal-deep:#2a9f90;
    --teal-soft:#67d7c9;
    --teal-pale:#c6efe9;
    --mint-wash:#e9f9f6;
    --ink:#1c1c1c;
    --text:#333;
    --paper:#f5f6f6;
    --paper-edge:#e7ebea;
    --line:#9a9a9a;
    --violet-pale:#e3daeb;
    --white:#ffffff;
  }
  *{box-sizing:border-box;margin:0;padding:0}
  html,body{width:729px;height:1200px;overflow:hidden}
  body{background:var(--backdrop);font-family:"Lato",sans-serif;color:var(--text);position:relative}
  .spread{position:absolute;left:64px;width:600px;height:440px;display:flex;box-shadow:0 6px 18px rgba(0,60,50,.25)}
  .spread--cover{top:78px}
  .spread--inside{top:676px}
  .page{position:relative;width:300px;height:440px;overflow:hidden;
    background:linear-gradient(135deg,var(--white) 0%,var(--paper) 55%,var(--paper-edge) 100%)}
  .page > *{position:absolute}
  .soft-circle{border-radius:50%;background:rgba(220,226,226,.55)}
  .serif{font-family:"Playfair Display",serif}
  .script{font-family:"Great Vibes",cursive}
  .page-title{font-family:"Playfair Display",serif;font-weight:600;color:var(--ink);font-size:22px;letter-spacing:.3px;line-height:1.35}

  /* care plan page */
  .care-title{left:0;width:300px;top:30px;text-align:center}
  .care-subtitle{left:0;width:300px;top:56px;text-align:center;font-size:21px;color:var(--ink)}
  .plan-box{left:26px;top:91px;width:241px;height:127px;background:rgba(255,255,255,.85);border:1px solid #d8dcdc;border-radius:9px}
  .plan-box > *{position:absolute}
  .plan-label{left:14px;top:14px;font-size:7.5px}
  .plan-line{height:1px;background:var(--line)}
  .plan-heading{left:14px;top:58px;font-size:9.5px;color:var(--ink)}
  .plan-field{font-size:7.5px}
  .support-title{left:0;width:300px;top:238px;text-align:center;font-family:"Playfair Display",serif;font-weight:700;font-size:15px;color:var(--ink)}
  .support-text{left:0;width:300px;top:265px;text-align:center;color:var(--teal);font-size:7px;line-height:2}
  .support-rule{left:43px;top:305px;width:197px;height:1px;background:#666}
  .contact{left:26px;top:339px;font-size:5.6px;color:var(--ink);border-collapse:collapse}
  .contact td{padding:0 0 8px 0;vertical-align:top;line-height:1.4}
  .contact td:first-child{width:30px}
  .thanks{left:192px;top:336px;width:90px;font-size:15px;color:var(--teal-soft);line-height:1.1;text-align:center}
  .wave{left:0;bottom:0}

  /* cover */
  .logo-ring{left:411px;top:44px;width:72px;height:72px;border:3px solid var(--teal);border-radius:50%}
  .brand-name{left:0;width:300px;top:137px;text-align:center;font-family:"Playfair Display",serif;font-weight:600;font-size:19px;color:var(--ink)}
  .brand-tag{left:0;width:300px;top:164px;text-align:center;font-size:8.5px;font-weight:700;letter-spacing:1.6px;color:var(--teal-deep)}
  .cover-photo{left:0;top:0}
  .cover-rule{left:107px;top:192px;width:80px;height:2px;background:var(--teal)}
  .cover-banner{left:43px;top:235px;width:204px;height:56px;border-radius:4px;background:rgba(61,181,165,.78);color:var(--white);text-align:center;font-family:"Playfair Display",serif;padding-top:8px}
  .cover-banner .small{font-size:11px;display:block}
  .cover-banner .large{font-size:14.5px;display:block;margin-top:3px}

  /* after treatment */
  .expect-title{left:31px;top:24px}
  .expect-sub{left:31px;top:59px;font-family:"Playfair Display",serif;font-size:11px;letter-spacing:1.6px;color:var(--teal)}
  .short-rule{height:2px;background:var(--teal)}
  .intro{left:31px;top:95px;width:170px;font-size:6.8px;color:var(--ink);line-height:1.7}
  .intro p + p{margin-top:4px}
  .tip{left:30px;width:170px;height:46px}
  .tip-icon{position:absolute;left:0;top:0;width:30px;height:30px;border-radius:50%;background:var(--teal);display:flex;align-items:center;justify-content:center}
  .tip-title{position:absolute;left:40px;top:-1px;font-size:11px;font-weight:700;color:var(--teal-deep);letter-spacing:-.2px}
  .tip-text{position:absolute;left:40px;top:15px;width:125px;font-size:6.8px;line-height:1.5;color:var(--ink)}
  .room-photo{left:181px;top:163px}
  .note-box{left:30px;top:351px;width:172px;height:47px;border-radius:7px;background:linear-gradient(90deg,var(--teal-soft),var(--teal));display:flex;align-items:center;padding-left:6px;color:var(--white);font-style:italic;font-size:7.5px;line-height:1.8}
  .note-box svg{margin-right:8px;flex:none}

  /* recovery */
  .journey-title{left:31px;top:24px}
  .journey-lead{left:31px;top:94px;width:150px;font-size:9.5px;color:var(--teal-deep);line-height:1.3}
  .sprig{left:143px;top:146px}
  .phase{top:182px;width:88px;height:133px;background:rgba(255,255,255,.9);border-radius:6px;text-align:center}
  .phase > *{position:absolute;left:0;width:100%}
  .phase-icon{left:29px !important;width:30px !important;top:9px;height:30px;border:2px solid var(--teal);border-radius:50%;display:flex;align-items:center;justify-content:center}
  .phase-name{top:48px;font-size:8.5px;color:var(--teal-deep)}
  .phase-step{top:60px;font-size:6.5px;font-weight:700;color:var(--ink)}
  .phase-list{top:79px;list-style:none;text-align:left;padding-left:6px}
  .phase-list li{font-size:5px;color:var(--text);margin-bottom:7px;padding-left:7px;position:relative}
  .phase-list li::before{content:"";position:absolute;left:0;top:1.5px;width:3.5px;height:3.5px;border-radius:50%;background:var(--teal-deep)}
  .promise-bar{left:19px;top:349px;width:271px;height:46px;border-radius:7px;background:linear-gradient(90deg,var(--teal),var(--teal-soft));display:flex;align-items:center;justify-content:space-around;color:var(--white);font-size:6.5px;line-height:1.9;padding:0 6px}
  .promise{display:flex;align-items:center;gap:7px}
</style>
</head>
<body>

<!-- Cover spread: care plan (back) + front cover -->
<section class="spread spread--cover">
  <article class="page page--care-plan">
    <div class="soft-circle" style="left:150px;top:-40px;width:190px;height:190px;background:rgba(240,244,220,.6)"></div>
    <h1 class="page-title care-title">YOUR PERSONAL</h1>
    <div class="script care-subtitle">Care Plan</div>

    <div class="plan-box">
      <span class="plan-label">Patient Name:</span>
      <span class="plan-line" style="left:14px;top:41px;width:202px"></span>
      <span class="plan-heading">Your Suggested Care Plan:</span>
      <span class="plan-line" style="left:16px;top:92px;width:49px"></span>
      <span class="plan-field" style="left:73px;top:84px">Treatments Over</span>
      <span class="plan-line" style="left:16px;top:113px;width:49px"></span>
      <span class="plan-field" style="left:73px;top:105px">Weeks</span>
    </div>

    <h2 class="support-title">We’re Here To Support You</h2>
    <p class="support-text">Your Health Journey Is Important To Us.<br>We’re With You Every Step Of The Way.</p>
    <span class="support-rule"></span>

    <table class="contact">
      <tr><td>Email:</td><td>info@fernwellpractice.com</td></tr>
      <tr><td>Website:</td><td>www.fernwellpractice.com</td></tr>
      <tr><td>Address:</td><td>chiropractic &amp; wellness 12 alder row,<br>marlow sl7 4qp</td></tr>
    </table>
    <div class="script thanks">Thank You For<br>Trusting Us</div>

    <svg class="wave" width="300" height="60" viewBox="0 0 300 60">
      <path d="M0 12 C40 2 80 30 140 32 C200 34 250 20 300 22 L300 60 L0 60 Z" fill="var(--teal)"/>
      <line x1="247" y1="35" x2="300" y2="35" stroke="#fff" stroke-width="2"/>
      <line x1="260" y1="46" x2="300" y2="46" stroke="#fff" stroke-width="2"/>
    </svg>
  </article>

  <article class="page page--front">
    <div class="soft-circle" style="left:-40px;top:-60px;width:200px;height:200px;background:rgba(205,212,212,.6)"></div>
    <svg class="cover-photo" width="300" height="440" viewBox="0 0 300 440">
      <defs>
        <linearGradient id="treatmentRoom" x1="0" y1="0" x2="0.6" y2="1">
          <stop offset="0" stop-color="#e8e4dc"/>
          <stop offset=".45" stop-color="#cfc6b6"/>
          <stop offset=".75" stop-color="#b9c9cc"/>
          <stop offset="1" stop-color="#d9d6d0"/>
        </linearGradient>
      </defs>
      <g role="img" aria-label="Photo of a bright clinic treatment room with a treatment table, desk and chairs">
        <path d="M0 180 L300 180 L300 380 C240 400 200 420 150 440 L0 440 Z" fill="url(#treatmentRoom)"/>
      </g>
      <path d="M0 418 C60 400 110 430 160 436 L0 440 Z" fill="var(--teal)"/>
      <path d="M150 440 C210 420 260 405 300 372 L300 440 Z" fill="var(--teal)"/>
    </svg>
    <span class="logo-ring" style="left:111px"></span>
    <div class="brand-name">FERNWELL PRACTICE</div>
    <div class="brand-tag">CHIROPRACTIC &amp; WELLNESS</div>
    <span class="cover-rule"></span>
    <div class="cover-banner">
      <span class="small">Your Journey To</span>
      <span class="large">Better Health Starts Here.</span>
    </div>
  </article>
</section>

<!-- Inside spread -->
<section class="spread spread--inside">
  <article class="page page--aftercare">
    <div class="soft-circle" style="left:150px;top:-50px;width:230px;height:230px"></div>
    <h2 class="page-title expect-title">WHAT TO EXPECT</h2>
    <div class="expect-sub">AFTER YOUR TREATMENT</div>
    <span class="short-rule" style="left:31px;top:83px;width:31px"></span>
    <div class="intro">
      <p>It’s Completely Normal To Feel Different After Your Session.</p>
      <p>Your Body Has Begun The Process Of Change And Healing.</p>
    </div>
    <span class="short-rule" style="left:31px;top:156px;width:76px;height:2.5px"></span>

    <svg class="room-photo" width="119" height="277" viewBox="0 0 119 277">
      <defs>
        <linearGradient id="calmRoom" x1="0" y1="0" x2="0" y2="1">
          <stop offset="0" stop-color="#e6e3e2"/>
          <stop offset=".6" stop-color="#d5d3d4"/>
          <stop offset="1" stop-color="#c4c2c0"/>
        </linearGradient>
      </defs>
      <g role="img" aria-label="Photo of a calm treatment room with a white treatment chair and framed artwork">
        <path d="M119 0 L60 0 C20 20 0 60 0 110 L0 277 L119 277 Z" fill="url(#calmRoom)"/>
      </g>
    </svg>

    <div class="tip" style="top:173px">
      <span class="tip-icon"><svg width="16" height="16" viewBox="0 0 16 16"><circle cx="8" cy="8" r="6.5" fill="none" stroke="#fff" stroke-width="1.3"/><path d="M8 4 C10 7 11 8.5 11 10 A3 3 0 0 1 5 10 C5 8.5 6 7 8 4Z" fill="none" stroke="#fff" stroke-width="1.2"/></svg></span>
      <span class="tip-title">STAY HYDRATED</span>
      <span class="tip-text">Drink Plenty Of Water To Support Your Body’s Recovery.</span>
    </div>
    <div class="tip" style="top:231px">
      <span class="tip-icon"><svg width="16" height="16" viewBox="0 0 16 16"><path d="M2 3 V13 M2 10 H14 V13 M6 10 V7 H13 A1.5 1.5 0 0 1 14 8.5 V10" fill="none" stroke="#fff" stroke-width="1.4"/><circle cx="4.5" cy="7.5" r="1.5" fill="#fff"/></svg></span>
      <span class="tip-title">ALLOW TIME TO REST</span>
      <span class="tip-text">Your Body May Need Time To Adjust- Listen To It.</span>
    </div>
    <div class="tip" style="top:287px">
      <span class="tip-icon"><svg width="16" height="16" viewBox="0 0 16 16"><circle cx="8" cy="3" r="1.8" fill="#fff"/><path d="M4 6 H12 M8 6 V10 M8 10 L6 15 M8 10 L10 15" stroke="#fff" stroke-width="1.6" fill="none" stroke-linecap="round"/></svg></span>
      <span class="tip-title">TAKE IT EASY</span>
      <span class="tip-text">Avoid Overexertion If You Feel Your Body Needs Recovery.</span>
    </div>

    <div class="note-box">
      <svg width="26" height="24" viewBox="0 0 26 24"><path d="M13 21 C4 14 2 10 2 7 A5.5 5.5 0 0 1 13 5 A5.5 5.5 0 0 1 24 7 C24 10 22 14 13 21Z" fill="none" stroke="#fff" stroke-width="1.6"/></svg>
      <span>Every Response Is Unique-<br>This Is A Positive Step Forward.</span>
    </div>
  </article>

  <article class="page page--journey">
    <div class="soft-circle" style="left:-60px;top:-90px;width:230px;height:230px;background:rgba(205,212,212,.55)"></div>
    <h2 class="page-title journey-title">YOUR RECOVERY<br>JOURNEY</h2>
    <p class="journey-lead">Healing is not a quick fix—it’s a guided journey.</p>
    <span class="short-rule" style="left:31px;top:131px;width:32px"></span>
    <svg class="sprig" width="20" height="24" viewBox="0 0 20 24"><path d="M4 22 C8 16 12 10 16 3" stroke="var(--teal)" stroke-width="1" fill="none"/><ellipse cx="14" cy="7" rx="2.2" ry="4" transform="rotate(35 14 7)" fill="none" stroke="var(--teal)" stroke-width=".9"/><ellipse cx="8" cy="15" rx="2" ry="3.5" transform="rotate(-40 8 15)" fill="none" stroke="var(--teal)" stroke-width=".9"/></svg>

    <div class="phase" style="left:19px">
      <span class="phase-icon"><svg width="14" height="14" viewBox="0 0 14 14"><circle cx="7" cy="7" r="3" fill="var(--teal)"/><path d="M7 1 V3 M7 11 V13 M1 7 H3 M11 7 H13" stroke="var(--teal)" stroke-width="1.2"/></svg></span>
      <span class="phase-name">Weeks 1–6</span>
      <span class="phase-step">(Phase 1)</span>
      <ul class="phase-list"><li>Initial improvements</li><li>Your body begins adapting</li></ul>
    </div>
    <div class="phase" style="left:109px">
      <span class="phase-icon"><svg width="14" height="14" viewBox="0 0 14 14"><path d="M2 10 C5 12 9 12 12 9" stroke="var(--teal)" stroke-width="1.4" fill="none"/><path d="M7 8 C5 6 5 3 8 2 C9 5 9 7 7 8Z" fill="var(--teal)"/></svg></span>
      <span class="phase-name">Weeks 6–12</span>
      <span class="phase-step">(Phase 2)</span>
      <ul class="phase-list"><li>Deeper correction &amp; progress</li><li>Building stability</li></ul>
    </div>
    <div class="phase" style="left:202px">
      <span class="phase-icon"><svg width="14" height="14" viewBox="0 0 14 14"><path d="M7 1 L12 3 V7 C12 10 10 12 7 13 C4 12 2 10 2 7 V3 Z" fill="none" stroke="var(--teal)" stroke-width="1.3"/><path d="M7 5 V9 M5 7 H9" stroke="var(--teal)" stroke-width="1.3"/></svg></span>
      <span class="phase-name">Wellness Phase</span>
      <span class="phase-step">(Maintenance)</span>
      <ul class="phase-list"><li>Long-term health</li><li>Prevention &amp; balance</li></ul>
    </div>

    <div class="promise-bar">
      <div class="promise"><svg width="22" height="22" viewBox="0 0 22 22"><circle cx="9" cy="6" r="4" fill="none" stroke="#fff" stroke-width="1.4"/><path d="M2 20 C2 14 5 12 9 12" fill="none" stroke="#fff" stroke-width="1.4"/><path d="M15 20 C11 17 11 15 13 14 C14 13.5 15 14 15 15 C15 14 16 13.5 17 14 C19 15 19 17 15 20Z" fill="none" stroke="#fff" stroke-width="1.2"/></svg><span>Your plan is<br>personalised</span></div>
      <div class="promise"><svg width="22" height="22" viewBox="0 0 22 22"><circle cx="11" cy="8" r="6" fill="none" stroke="#fff" stroke-width="1.4"/><path d="M11 5 V8 L13 10" stroke="#fff" stroke-width="1.3" fill="none"/><rect x="3" y="17" width="16" height="3" rx="1.5" fill="none" stroke="#fff" stroke-width="1.2"/></svg><span>Progress<br>takes time</span></div>
      <div class="promise"><svg width="22" height="22" viewBox="0 0 22 22"><path d="M4 11 A7 7 0 0 1 16 5 M18 11 A7 7 0 0 1 6 17" fill="none" stroke="#fff" stroke-width="1.4"/><path d="M16 2 V5 H13 M6 20 V17 H9" fill="none" stroke="#fff" stroke-width="1.3"/><path d="M8 11 L10 13 L14 9" fill="none" stroke="#fff" stroke-width="1.4"/></svg><span>Consistency =<br>results</span></div>
    </div>
  </article>
</section>

</body>
</html>
```